Lanternwick Pathway Ledger Basics

size of the ad - 8”x 10.75" plus 0.25" bleed
I would like an ad for a magazine that will stand out and make people want to read the ad.
The ad should not be crowded and people reading the ad will be able to read the text.
I would like it to be a creative and modern-day design.
the list of topics should not be the focus of the ad.
the text is attached.
If you decide to use people in the ad then please no ladies.
please note that leave over 1 inch for the bottom of the footer

```html
<!DOCTYPE html>
<html lang="en">
<head>
<meta charset="utf-8">
<title>Real Estate Course Ad</title>
<link rel="stylesheet" href="https://fonts.googleapis.com/css2?family=Bebas+Neue&family=Poppins:wght@400;500;600;700;800&display=swap">
<style>
  :root {
    --red: #d90f1f;
    --navy: #0c1766;
    --ink: #3a3a44;
    --paper: #ffffff;
    --backdrop: #ececec;
  }
  * { margin: 0; padding: 0; box-sizing: border-box; }
  html, body { width: 1200px; height: 2925px; overflow: hidden; background: var(--backdrop); }
  .ad-page {
    position: absolute; left: 60px; top: 742px; width: 1080px; height: 1440px;
    background: var(--paper); box-shadow: 0 10px 40px rgba(0,0,0,.25); overflow: hidden;
    font-family: 'Poppins', sans-serif;
  }
  .headline { position: absolute; left: 0; top: 0; width: 1080px; height: 250px; }
  .headline .course-title { font-family: 'Bebas Neue', sans-serif; fill: var(--red); }
  .headline .course-subtitle { font-family: 'Poppins', sans-serif; font-weight: 700; fill: var(--navy); }
  .hero-photo {
    position: absolute; left: 0; top: 245px; width: 1080px; height: 497px;
    background: linear-gradient(180deg, #ffffff 0%, #e7ebee 22%, #c8cfd2 42%, #a9aea3 58%, #7f8f7a 72%, #6f7d70 86%, #5e6b60 100%);
  }
  .tagline-band {
    position: absolute; left: 0; top: 742px; width: 1080px; height: 85px; background: var(--navy);
    color: #fff; font-size: 36px; font-weight: 500; line-height: 85px; padding-left: 72px; letter-spacing: .2px;
  }
  .event-details { position: absolute; left: 72px; top: 850px; width: 560px; }
  .event-location { font-size: 86px; font-weight: 800; color: var(--red); line-height: 1; letter-spacing: 1px; }
  .event-schedule { margin-top: 18px; font-size: 44px; font-weight: 700; line-height: 1; }
  .event-schedule .sessions-count { color: var(--navy); display: block; }
  .event-schedule .sessions-type { color: var(--ink); display: block; margin-top: 2px; }
  .start-date {
    margin-top: 20px; display: flex; width: 482px; height: 70px; border: 3px solid var(--red); border-radius: 12px; overflow: hidden;
  }
  .start-date .label { background: #fff; color: var(--ink); font-weight: 700; font-size: 32px; padding: 0 12px; line-height: 64px; letter-spacing: 1px; }
  .start-date .date {
    flex: 1; background: var(--navy); color: #fff; font-family: 'Bebas Neue', sans-serif; font-size: 56px; line-height: 68px; padding-left: 14px;
  }
  .start-date .date sup { font-size: 26px; vertical-align: 22px; }
  .scholarships { margin-top: 18px; font-size: 29px; font-weight: 700; color: var(--ink); }
  .early-bird { margin-top: 6px; font-size: 40px; font-weight: 700; color: var(--navy); line-height: 1.1; }
  .audience { margin-top: 6px; font-size: 31px; font-weight: 500; color: var(--ink); line-height: 1.15; }
  .topics { position: absolute; left: 668px; top: 856px; width: 390px; }
  .topics h2 { font-size: 24px; font-weight: 700; color: var(--navy); margin-bottom: 14px; }
  .topics ul { list-style: none; }
  .topics li { display: flex; align-items: center; height: 41.6px; font-size: 16.5px; color: var(--navy); font-weight: 500; }
  .topics li svg { width: 16px; height: 16px; margin: 0 14px 0 4px; flex: none; }
</style>
</head>
<body>
  <main class="ad-page">
    <svg class="headline" viewBox="0 0 1080 250">
      <text class="course-title" x="70" y="181" font-size="158" textLength="934" lengthAdjust="spacingAndGlyphs">REAL ESTATE COURSE</text>
      <text class="course-subtitle" x="72" y="230" font-size="40" textLength="930" lengthAdjust="spacingAndGlyphs">LANTERNWICK PATHWAY LEDGER BASICS</text>
    </svg>

    <div class="hero-photo" role="img" aria-label="Photo of an open hand holding a cluster of high-rise buildings with a construction crane above an aerial city view"></div>

    <div class="tagline-band">Investing in Knowledge is investing in Opportunities.</div>

    <section class="event-details">
      <div class="event-location">MONSEY</div>
      <div class="event-schedule">
        <span class="sessions-count">10 -TUESDAY</span>
        <span class="sessions-type">EVENINGS SESSIONS</span>
      </div>
      <div class="start-date">
        <span class="label">STARTING</span>
        <span class="date">28<sup>TH</sup> FEBRUARY</span>
      </div>
      <div class="scholarships">LIMITED PARTIAL SCHOLARSHIPS</div>
      <div class="early-bird">EARLY BIRD SPECIAL</div>
      <div class="audience">For those that started or would<br>like to go into real estate</div>
    </section>

    <section class="topics">
      <h2>TOPICS: PARTIAL LISTING</h2>
      <ul>
        <li><svg viewBox="0 0 16 16"><circle cx="8" cy="8" r="6.8" fill="none" stroke="#0c1766" stroke-width="1.4"/><path d="M5 8.2l2 2 4-4" fill="none" stroke="#0c1766" stroke-width="1.4"/></svg>Real estate investment strategies</li>
        <li><svg viewBox="0 0 16 16"><circle cx="8" cy="8" r="6.8" fill="none" stroke="#0c1766" stroke-width="1.4"/><path d="M5 8.2l2 2 4-4" fill="none" stroke="#0c1766" stroke-width="1.4"/></svg>Due diligence</li>
        <li><svg viewBox="0 0 16 16"><circle cx="8" cy="8" r="6.8" fill="none" stroke="#0c1766" stroke-width="1.4"/><path d="M5 8.2l2 2 4-4" fill="none" stroke="#0c1766" stroke-width="1.4"/></svg>Financing</li>
        <li><svg viewBox="0 0 16 16"><circle cx="8" cy="8" r="6.8" fill="none" stroke="#0c1766" stroke-width="1.4"/><path d="M5 8.2l2 2 4-4" fill="none" stroke="#0c1766" stroke-width="1.4"/></svg>Underwriting</li>
        <li><svg viewBox="0 0 16 16"><circle cx="8" cy="8" r="6.8" fill="none" stroke="#0c1766" stroke-width="1.4"/><path d="M5 8.2l2 2 4-4" fill="none" stroke="#0c1766" stroke-width="1.4"/></svg>Property management</li>
        <li><svg viewBox="0 0 16 16"><circle cx="8" cy="8" r="6.8" fill="none" stroke="#0c1766" stroke-width="1.4"/><path d="M5 8.2l2 2 4-4" fill="none" stroke="#0c1766" stroke-width="1.4"/></svg>Real estate Legal basics</li>
        <li><svg viewBox="0 0 16 16"><circle cx="8" cy="8" r="6.8" fill="none" stroke="#0c1766" stroke-width="1.4"/><path d="M5 8.2l2 2 4-4" fill="none" stroke="#0c1766" stroke-width="1.4"/></svg>Sourcing deals</li>
        <li><svg viewBox="0 0 16 16"><circle cx="8" cy="8" r="6.8" fill="none" stroke="#0c1766" stroke-width="1.4"/><path d="M5 8.2l2 2 4-4" fill="none" stroke="#0c1766" stroke-width="1.4"/></svg>Syndication</li>
        <li><svg viewBox="0 0 16 16"><circle cx="8" cy="8" r="6.8" fill="none" stroke="#0c1766" stroke-width="1.4"/><path d="M5 8.2l2 2 4-4" fill="none" stroke="#0c1766" stroke-width="1.4"/></svg>Dealing with brokers</li>
        <li><svg viewBox="0 0 16 16"><circle cx="8" cy="8" r="6.8" fill="none" stroke="#0c1766" stroke-width="1.4"/><path d="M5 8.2l2 2 4-4" fill="none" stroke="#0c1766" stroke-width="1.4"/></svg>Tax fundamentals</li>
      </ul>
    </section>
  </main>
</body>
</html>
```